Disposable Mini Sauce Pot Design for Asian Chain Food Brands

We operate a Hainan Chicken Rice takeout brand under the name Wokly8, with our official website: www.Wokly8.com.
We offer four signature house sauces and are launching brand-new packaging for our sauce line. We require custom graphic designs exclusively for the sauce cup lids.
Product Material & Base Specs
The sauce cups are made of PP plastic, available in two translucent base options: Translucent White and Translucent Orange.
Four Sauce Varieties for Individual Lid Designs
1. Red Sauce – Fried Sweet Chili Sauce
2.Green Sauce – Scallion Oil Dressing
3.Sweet Soy Sauce
4.Sweet Red Sauce (Special for Fried Chicken)
Differentiate each sauce lid design through unique graphics, typography, or illustrative elements for easy customer identification.
The marking NET WT 2 OZ must be clearly printed on every lid.
**There is no need to print full descriptive text or the full name of the sauces on each lid; the design only needs to clearly differentiate the four sauce varieties.
**Please reference the original design style and brand color palette shown on our official website, and feel free to fully unleash your creativity.
Look and feel
Each slider illustrates characteristics of the customer's brand and the style your logo design should communicate.

```html
<!DOCTYPE html>
<html lang="en">
<head>
<meta charset="utf-8">
<title>Wokly8 Sauce Lid Labels</title>
<link href="https://fonts.googleapis.com/css2?family=Titan+One&family=Archivo+Black&display=swap" rel="stylesheet">
<style>
  :root {
    --page-bg: #f6f6f6;
    --red: #d9251f;
    --green: #8cc63f;
    --scallion: #6ea42e;
    --soy: #231f20;
    --orange: #ef7d1a;
    --soy-orange: #e8731c;
    --ink-light: #ffffff;
  }
  * { box-sizing: border-box; margin: 0; padding: 0; }
  html, body { width: 1149px; height: 1200px; overflow: hidden; }
  body {
    background: var(--page-bg);
    display: flex;
    align-items: center;
    justify-content: center;
    gap: 40px;
    font-family: "Titan One", "Archivo Black", sans-serif;
  }
  .lid-label {
    position: relative;
    width: 240px;
    height: 270px;
    padding-top: 6px;
    border-radius: 12px;
    overflow: hidden;
    color: var(--ink-light);
    box-shadow: 6px 8px 14px rgba(0,0,0,.35);
    display: flex;
    flex-direction: column;
    align-items: center;
    text-align: center;
  }
  .lid-label--red { background: var(--red); }
  .lid-label--green { background: var(--green); }
  .lid-label--soy { background: var(--soy); }
  .lid-label--sweet-red { background: var(--orange); }

  .word { line-height: .9; letter-spacing: -1px; white-space: nowrap; }
  .word--xl { font-size: 84px; }
  .word--lg { font-size: 68px; }
  .word--md { font-size: 56px; }
  .accent { color: var(--soy-orange); }

  .flavor { font-size: 15px; line-height: 1.1; margin: 4px 0 6px; }
  .blurb {
    font-family: "Archivo Black", sans-serif;
    font-size: 9px;
    letter-spacing: 2px;
    margin-top: 8px;
  }
  .scallion-art {
    width: 170px;
    height: 14px;
    margin: 8px 0 6px;
    background: linear-gradient(90deg, var(--scallion), rgba(110,164,46,.4));
    border-radius: 7px;
  }
  .lid-footer {
    position: absolute;
    left: 18px; right: 14px; bottom: 14px;
    display: flex;
    justify-content: space-between;
    align-items: flex-end;
  }
  .brand { font-size: 14px; line-height: 1; }
  .net-wt { font-family: "Archivo Black", sans-serif; font-size: 12px; }
</style>
</head>
<body>

  <section class="lid-label lid-label--red">
    <div class="word word--xl">Red</div>
    <p class="flavor">Fried<br>Sweet Chili</p>
    <div class="word word--lg">Sauce</div>
    <p class="blurb">Lorem ipsum dolor sit amet,</p>
    <div class="lid-footer">
      <span class="brand">Wokly8</span>
      <span class="net-wt">NET WT 2 OZ</span>
    </div>
  </section>

  <section class="lid-label lid-label--green">
    <div class="word word--md">Green</div>
    <div class="word word--lg">Sauce</div>
    <div class="scallion-art" role="img" aria-label="Scallion stalk illustration"></div>
    <p class="flavor">Scallion Oil Dressing</p>
    <p class="blurb">Lorem ipsum dolor sit amet,</p>
    <div class="lid-footer">
      <span class="brand">Wokly8</span>
      <span class="net-wt">NET WT 2 OZ</span>
    </div>
  </section>

  <section class="lid-label lid-label--soy">
    <div class="word word--md accent">Sweet</div>
    <div class="word word--xl">Soy</div>
    <div class="word word--md accent">Sauce</div>
    <div class="lid-footer">
      <span class="brand">Wokly8</span>
      <span class="net-wt">NET WT 2 OZ</span>
    </div>
  </section>

  <section class="lid-label lid-label--sweet-red">
    <div class="word word--md">Sweet</div>
    <div class="word word--xl">Red</div>
    <div class="word word--md">Sauce</div>
    <p class="flavor" style="margin-top:8px">Special for Fried Chicken</p>
    <div class="lid-footer">
      <span class="brand">Wokly8</span>
      <span class="net-wt">NET WT 2 OZ</span>
    </div>
  </section>

</body>
</html>
```